Menu: A4 (double sided) Lunch/Dinner Menu (one side) + Pizza Menu (other side)

Hello.
We would like to create a new style of menus.
Must be easy to read - a summer feel, crisp, clean, beachy, possible retro feel, colours probably based on our website colours (see address below).
Simple and casual is best as we are a casual beachside Cafe.
This menu will be double sided therefore this job is 2 pages.
If you win this job we will have 2 or 3 more menus for you to create soon after (Drinks, Breakfast, possibly a small Kids menu).
The paper for these menus we expect will be a nice white paper which will then be matte laminated.
Colours possible are the green colour #3a6066, the terracotta on our website logo border and website buttons, maybe a little yellow but must be easy to read on white paper.
Black for text might be okay if this is your best design option.
Please view our website and take a feel for the business, location, the existing website branding and website colours we are trying to achieve, www.tidelinekitchen.com.au
We prefer to avoid overwhelming the guest with too many colours on the menus (hence the white paper) as the building is so colourful (El Prado, Argentina, inspired) and the guest experience can be complimented via crisp easy to read menus.
IMPORTANT:
The menus provided please must be fully and easily editable by us in the future.
If you win the job, you must please provide clear instructions on how our staff can edit the menus in the future if project is delivered in Adobe format. Word is also an option for us if you like.
As such, we have attached some documents: the 2x Word documents for the text, 2x .pdf so you can see the fonts and style we were using previously (was printing on recycled brown paper then matte laminated).
If you wished to use the SeaLife Font (this is the existing Font for headings) please let us know as we purchased that font and can provide it.
We have also attached a menu from Marlowe Tavern which we feel has a nice retro feel.
Please include our Instagram in 1 place on the menu @tidelinekitchen
Finally, please note,
we never wish to waste anyone's time so we will narrow down the submissions quickly based on first drafts (please know this is because we appreciate your effort and know your time is valuable) and we will then work with the top designer to finalise in a professional fashion.
Thank you.

```html
<!DOCTYPE html>
<html lang="en">
<head>
<meta charset="utf-8">
<title>Tideline Kitchen – Lunch + Dinner and Pizza Menus</title>
<link rel="stylesheet" href="https://fonts.googleapis.com/css2?family=Archivo+Black&family=Montserrat:wght@400;500;600;700;800&display=swap">
<style>
:root{
  --canvas:#e9e9e9;
  --paper:#fbf8f2;
  --paper-shade:#f1ebe0;
  --ink:#1d1d1d;
  --sea-green:#3a6066;
  --terracotta:#c2603e;
  --sand-yellow:#e9c94a;
  --shell:#f3e6d3;
}
*{box-sizing:border-box;margin:0;padding:0}
html,body{width:1200px;height:3071px;overflow:hidden}
body{background:var(--canvas);font-family:"Montserrat",Arial,sans-serif;color:var(--ink);position:relative}

.menu-page{position:absolute;left:265px;width:670px;
  background:radial-gradient(ellipse at 30% 20%,var(--paper) 0%,var(--paper-shade) 100%);
  box-shadow:0 2px 6px rgba(0,0,0,.12)}
.menu-page--lunch{top:912px;height:950px}
.menu-page--pizza{top:1970px;height:952px}

.edge-stripe{position:absolute;top:0;bottom:0;width:8px;
  background:repeating-linear-gradient(180deg,
    var(--sea-green) 0 22px,var(--terracotta) 22px 44px,
    var(--sand-yellow) 44px 66px,var(--shell) 66px 88px)}
.edge-stripe--left{left:0}
.edge-stripe--right{right:0}

.frame{position:absolute;inset:0;width:100%;height:100%;pointer-events:none}

.brand-name{position:absolute;left:0;right:0;top:66px;text-align:center;
  font-family:"Montserrat",sans-serif;font-weight:800;font-size:34px;
  letter-spacing:2px;color:var(--sea-green);text-transform:uppercase;line-height:1.05}
.brand-name .square{display:inline-block;width:12px;height:12px;background:var(--sea-green);margin-right:10px;vertical-align:middle}

.art{position:absolute;border-radius:6px}
.art--burger{left:76px;top:64px;width:78px;height:72px;background:linear-gradient(135deg,#ece6dc,#c9c1b4)}
.art--fries{left:485px;top:52px;width:86px;height:88px;background:linear-gradient(135deg,#eee8dd,#cdc5b8)}
.art--pizza-left{left:66px;top:78px;width:134px;height:100px;border-radius:50%;background:radial-gradient(circle,#e5ded1,#bdb3a4)}
.art--pizza-right{left:446px;top:78px;width:160px;height:92px;border-radius:50%;background:radial-gradient(circle,#d7cfc2,#a39a8c)}

.page-title{position:absolute;left:0;right:0;text-align:center;
  font-family:"Archivo Black",sans-serif;font-size:42px;letter-spacing:1px;line-height:1}
.menu-page--lunch .page-title{top:163px}
.menu-page--pizza .page-title{top:168px;font-size:34px}
.title-rule{position:absolute;left:122px;right:122px;top:211px;height:3px;background:var(--sea-green)}
.title-rule::before,.title-rule::after{content:"";position:absolute;top:-2.5px;width:8px;height:8px;border-radius:50%;background:var(--sea-green)}
.title-rule::before{left:-4px}.title-rule::after{right:-4px}
.page-subtitle{position:absolute;left:0;right:0;top:219px;text-align:center;font-size:10.5px;font-weight:500}

.section-title{position:absolute;left:0;right:0;text-align:center;font-weight:700;font-size:17px}
.section-title--green{color:var(--sea-green)}
.section-title--red{color:var(--terracotta)}
.section-title--boxed{left:50%;transform:translateX(-50%);right:auto;border:2px solid;padding:1px 5px;font-size:16px;white-space:nowrap}
.section-title--green-box{color:var(--sea-green);border-color:var(--sea-green)}
.section-title--red-box{color:var(--terracotta);border-color:var(--terracotta)}

.col-divider{position:absolute;left:334px;border-left:2px dotted var(--sea-green)}

.dish{position:absolute;width:250px;font-size:10.5px;line-height:12.5px}
.col-left{left:56px}
.col-right{left:346px;width:270px}
.dish-head{display:flex;align-items:baseline;gap:4px}
.dish-name{font-weight:700;font-size:11px;white-space:nowrap}
.dish-name.wrap{white-space:normal}
.dots{flex:1;border-bottom:1px dotted #555;transform:translateY(-3px);min-width:10px}
.price{font-weight:700;font-size:11px;width:22px;text-align:right}
.price sup{font-size:6.5px;vertical-align:5px}
.dish-desc{font-weight:500;width:190px}
.veg{color:var(--sea-green);font-weight:700}
.gfo{color:var(--terracotta);font-weight:700}
.heat{color:var(--terracotta);font-weight:600;font-size:10px}
.heat svg{vertical-align:-1px}
.mild{font-weight:500;color:var(--ink)}

.social{position:absolute;left:70px;top:862px;font-size:10.5px;font-weight:700;color:var(--sea-green)}
.turn-over{position:absolute;left:376px;top:862px;font-size:10.5px;font-weight:700;display:flex;align-items:center;gap:10px}
.turn-over .art-mini{width:28px;height:14px;border-radius:4px;background:linear-gradient(135deg,#e6e0d5,#bbb3a6)}

.legend{position:absolute;left:0;right:0;text-align:center;font-size:10px;font-weight:500;display:flex;justify-content:center;gap:26px}
.legend .sq{display:inline-block;width:7px;height:7px;margin-right:6px;vertical-align:1px}
.sq--green{background:var(--sea-green)}
.sq--terra{background:var(--terracotta)}
.legend .extra{color:var(--terracotta);font-weight:700}
.menu-page--lunch .legend{top:891px}
.menu-page--pizza .legend{top:894px;font-size:9px;gap:40px}

.allergy-note{position:absolute;left:107px;top:834px;width:466px;border:1.5px solid var(--ink);padding:4px 8px;font-size:8.6px;line-height:10.5px;font-weight:500}
.allergy-note strong{color:var(--terracotta);font-weight:700}
</style>
</head>
<body>

<section class="menu-page menu-page--lunch" aria-label="Lunch and dinner menu">
  <div class="edge-stripe edge-stripe--left"></div>
  <div class="edge-stripe edge-stripe--right"></div>
  <svg class="frame" viewBox="0 0 670 950" aria-hidden="true">
    <path d="M72 42 H598 A30 30 0 0 0 628 72 V880 A30 30 0 0 0 598 910 H72 A30 30 0 0 0 42 880 V72 A30 30 0 0 0 72 42 Z" fill="none" stroke="#1d1d1d" stroke-width="2.5"/>
  </svg>

  <div class="art art--burger" role="img" aria-label="Pencil sketch of a burger"></div>
  <div class="art art--fries" role="img" aria-label="Pencil sketch of a carton of fries"></div>
  <div class="brand-name"><span class="square"></span>Tideline<br>Kitchen</div>

  <h1 class="page-title">LUNCH + DINNER</h1>
  <div class="title-rule"></div>

  <h2 class="section-title section-title--green" style="top:231px">Entree</h2>
  <div class="col-divider" style="top:262px;height:142px"></div>

  <div class="dish col-left" style="top:266px"><div class="dish-head"><span class="dish-name">Garlic Bread (2) <span class="veg">v</span></span><span class="dots"></span><span class="price"><sup>$</sup>8</span></div></div>
  <div class="dish col-left" style="top:289px"><div class="dish-head"><span class="dish-name">Salt &amp; Pepper Squid</span><span class="dots"></span><span class="price"><sup>$</sup>18</span></div><p class="dish-desc">w/ thai dipping sauce</p></div>
  <div class="dish col-left" style="top:325px"><div class="dish-head"><span class="dish-name">Duo of Dip <span class="veg">v</span></span><span class="dots"></span><span class="price"><sup>$</sup>14</span></div><p class="dish-desc">w/ pita</p></div>
  <div class="dish col-left" style="top:360px"><div class="dish-head"><span class="dish-name">Bowl of Chips <span class="veg">v</span></span><span class="dots"></span><span class="price"><sup>$</sup>11</span></div><p class="dish-desc">w/ tomato sauce</p></div>

  <div class="dish col-right" style="top:266px"><div class="dish-head"><span class="dish-name">Seasoned Wedges <span class="veg">v</span></span><span class="dots"></span><span class="price"><sup>$</sup>15</span></div><p class="dish-desc">w/ sour cream &amp; sweet chilli</p></div>
  <div class="dish col-right" style="top:301px"><div class="dish-head"><span class="dish-name">Onion Rings (12) beer battered <span class="veg">v</span></span><span class="dots"></span><span class="price"><sup>$</sup>13</span></div><p class="dish-desc">w/ tangy mayo</p></div>
  <div class="dish col-right" style="top:338px"><div class="dish-head"><span class="dish-name">Vietnamese Spring Rolls (3)</span><span class="dots"></span><span class="price"><sup>$</sup>11</span></div><p class="dish-desc">chicken, home-made</p></div>
  <div class="dish col-right" style="top:374px"><div class="dish-head"><span class="dish-name">Bruschetta (1) <span class="veg">v</span></span><span class="dots"></span><span class="price"><sup>$</sup>10</span></div><p class="dish-desc">w/ olive oil, tomato &amp; red onion salsa,balsamic glaze, feta</p></div>

  <h2 class="section-title section-title--red" style="top:418px">Mains</h2>
  <div class="col-divider" style="top:456px;height:160px"></div>

  <div class="dish col-left" style="top:460px"><div class="dish-head"><span class="dish-name">The Fish $ Chips</span><span class="dots"></span><span class="price"><sup>$</sup>25</span></div><p class="dish-desc">house-crumbed butterfish w/ chips, tartare &amp; side salad</p></div>
  <div class="dish col-left" style="top:510px"><div class="dish-head"><span class="dish-name wrap">Smokey Beef &amp; Bacon<br>Cheese Burger</span><span class="dots"></span><span class="price"><sup>$</sup>23</span></div><p class="dish-desc">w/ chips, onion rings, gerkins &amp; tangy mayo + jalapenos (2) + pineapple (2)</p></div>
  <div class="dish col-left" style="top:585px"><div class="dish-head"><span class="dish-name">Salt &amp; Pepper Squid</span><span class="dots"></span><span class="price"><sup>$</sup>31</span></div><p class="dish-desc">golden tangles w/ chips, thai dipping sauce &amp; side salad</p></div>

  <div class="dish col-right" style="top:460px"><div class="dish-head"><span class="dish-name">Seafood Basket</span><span class="dots"></span><span class="price"><sup>$</sup>31</span></div><p class="dish-desc">crumbed butterfish, grilled prawns, salt &amp; pepper squid, chips, tartare &amp; side salad</p></div>
  <div class="dish col-right" style="top:523px"><div class="dish-head"><span class="dish-name">Atlantic Salmon</span><span class="dots"></span><span class="price"><sup>$</sup>31</span></div><p class="dish-desc">served w/ mash, teriyaki sauce &amp; winter vegetables</p></div>
  <div class="dish col-right" style="top:573px"><div class="dish-head"><span class="dish-name">Chicken Parmigiana</span><span class="dots"></span><span class="price"><sup>$</sup>27</span></div><p class="dish-desc">house-crumbed breast schnitzel, napoli sauce, mozzarella, chips &amp; side salad + bacon and pineapple 4 + jalapenos and pineapple 4</p></div>

  <h2 class="section-title section-title--boxed section-title--green-box" style="top:642px">TIDELINE PLATTER for 2</h2>
  <div class="col-divider" style="top:680px;height:170px"></div>

  <div class="dish col-left" style="top:684px"><div class="dish-head"><span class="dish-name">New York Serloin <span class="gfo">gfo</span></span><span class="dots"></span><span class="price"><sup>$</sup>38</span></div><p class="dish-desc">400g grass-fed w/ mash &amp; winter vegetables<br>choose: mushroom gravy or classic gravy</p></div>
  <div class="dish col-left" style="top:761px"><div class="dish-head"><span class="dish-name">Chicken Caesar</span><span class="dots"></span><span class="price"><sup>$</sup>27</span></div><p class="dish-desc">w/ bacon, anchovies, egg, caesar dressing, parmesan, spanish onion, garlic bread</p></div>
  <div class="dish col-left" style="top:812px"><div class="dish-head"><span class="dish-name">Lamb Salad <span class="gfo">gfo</span></span><span class="dots"></span><span class="price"><sup>$</sup>30</span></div><p class="dish-desc" style="width:220px">skewers w/ traditional greek salad, tzatziki &amp; garlic bread+ extra lamb 8</p></div>

  <div class="dish col-right" style="top:684px"><div class="dish-head"><span class="dish-name">Thai Chicken Curry <span class="gfo">gfo</span> <span class="heat"><svg width="6" height="10" viewBox="0 0 6 10"><path d="M4 0 C6 3 5 8 1 10 C3 7 3 4 4 0Z" fill="#c2603e"/></svg> <span class="mild">mild</span></span></span><span class="dots"></span><span class="price"><sup>$</sup>26</span></div><p class="dish-desc">traditional recipe, w/ jasmine rice &amp; papadums</p></div>
  <div class="dish col-right" style="top:734px"><div class="dish-head"><span class="dish-name">Beach Burger <span class="veg">v</span></span><span class="dots"></span><span class="price"><sup>$</sup>23</span></div><p class="dish-desc">house-made pea &amp; corn ricotta fritter, pineapple, w/ wedges, onion rings, sweet chilli</p></div>
  <div class="dish col-right" style="top:796px"><div class="dish-head"><span class="dish-name">Vegan Curry <span class="gfo">gfo</span> <span class="heat"><svg width="6" height="10" viewBox="0 0 6 10"><path d="M4 0 C6 3 5 8 1 10 C3 7 3 4 4 0Z" fill="#c2603e"/></svg> <span class="mild">mild</span></span></span><span class="dots"></span><span class="price"><sup>$</sup>24</span></div><p class="dish-desc">chickpea &amp; pumpkin w/ fresh tomatoes &amp; basil, jasmine rice &amp; papadums</p></div>

  <p class="social">Follow us @tidelinekitchen</p>
  <div class="turn-over"><span>For</span><span class="art-mini" role="img" aria-label="Small sketch of a pizza slice"></span><span>Please Turn over</span></div>

  <div class="legend"><span><span class="sq sq--green"></span><span class="veg">V</span> - Vegetarian</span><span><span class="sq sq--terra"></span><span class="gfo">gfo</span> - Gluten Friendly Optional, please ask</span></div>
</section>

<section class="menu-page menu-page--pizza" aria-label="Pizza menu">
  <div class="edge-stripe edge-stripe--left"></div>
  <div class="edge-stripe edge-stripe--right"></div>
  <svg class="frame" viewBox="0 0 670 952" aria-hidden="true">
    <path d="M72 42 H598 A30 30 0 0 0 628 72 V882 A30 30 0 0 0 598 912 H72 A30 30 0 0 0 42 882 V72 A30 30 0 0 0 72 42 Z" fill="none" stroke="#1d1d1d" stroke-width="2.5"/>
  </svg>

  <div class="art art--pizza-left" role="img" aria-label="Pencil sketch of a whole pizza with a slice cut"></div>
  <div class="art art--pizza-right" role="img" aria-label="Sketch of a pepperoni pizza with a slice lifted"></div>
  <div class="brand-name"><span class="square"></span>Tideline<br>Kitchen</div>

  <h1 class="page-title">PIZZA</h1>
  <p class="page-subtitle">ALL 12" with house-made tomato base &amp; mozzarella</p>

  <h2 class="section-title section-title--green" style="top:234px">Standard</h2>
  <div class="col-divider" style="top:264px;height:302px"></div>

  <div class="dish col-left" style="top:266px"><div class="dish-head"><span class="dish-name">Hawaiian</span><span class="dots"></span><span class="price"><sup>$</sup>22</span></div><p class="dish-desc">ham, pineapple</p></div>
  <div class="dish col-left" style="top:303px"><div class="dish-head"><span class="dish-name">Margherita <span class="veg">v</span></span><span class="dots"></span><span class="price"><sup>$</sup>22</span></div><p class="dish-desc" style="width:140px">marinated &amp; diced tomatoes, fresh basil</p></div>
  <div class="dish col-left" style="top:353px"><div class="dish-head"><span class="dish-name">BBQ Chicken</span><span class="dots"></span><span class="price"><sup>$</sup>26</span></div><p class="dish-desc" style="width:150px">chicken, salami, tomato, spanish onion, bbq sauce</p></div>
  <div class="dish col-left" style="top:403px"><div class="dish-head"><span class="dish-name">Chorizo</span><span class="dots"></span><span class="price"><sup>$</sup>26</span></div><p class="dish-desc" style="width:160px">chorizo, salami, tomato, mushrooms, spanish onion</p></div>
  <div class="dish col-left" style="top:453px"><div class="dish-head"><span class="dish-name">Tideline Special</span><span class="dots"></span><span class="price"><sup>$</sup>26</span></div><p class="dish-desc" style="width:150px">ham, salami, prawns, kalamata olives, roasted capsicum, mushrooms, spanish onion</p></div>
  <div class="dish col-left" style="top:530px"><div class="dish-head"><span class="dish-name">Meat Lovers</span><span class="dots"></span><span class="price"><sup>$</sup>26</span></div><p class="dish-desc" style="width:150px">chicken, bacon, salami, ham, bbq sauce</p></div>

  <div class="dish col-right" style="top:266px"><div class="dish-head"><span class="dish-name">Mona Lisa</span><span class="dots"></span><span class="price"><sup>$</sup>26</span></div><p class="dish-desc" style="width:180px">chicken, pineapple, ham, spanish onion, mushrooms</p></div>
  <div class="dish col-right" style="top:317px"><div class="dish-head"><span class="dish-name">Puttanesca</span><span class="dots"></span><span class="price"><sup>$</sup>26</span></div><p class="dish-desc" style="width:150px">anchovies, capers, salami, kalamata olives, roasted capsicum, parmesan</p></div>
  <div class="dish col-right" style="top:380px"><div class="dish-head"><span class="dish-name">Tropical Chicken</span><span class="dots"></span><span class="price"><sup>$</sup>26</span></div><p class="dish-desc" style="width:180px">chicken, pineapple, spanish onion, chilli, tomato, mushrooms</p></div>
  <div class="dish col-right" style="top:429px"><div class="dish-head"><span class="dish-name">Vegetarian <span class="veg">v</span></span><span class="dots"></span><span class="price"><sup>$</sup>26</span></div><p class="dish-desc" style="width:180px">roasted capsicum, tomato, mushrooms, artichokes, kalamata olives, spanish onion</p></div>
  <div class="dish col-right" style="top:495px"><div class="dish-head"><span class="dish-name">Build Your Own <span class="veg">v</span></span><span class="dots"></span><span class="price"><sup>$</sup>26</span></div><p class="dish-desc" style="width:180px">tomato base, mozzarella &amp; four toppings</p></div>

  <h2 class="section-title section-title--boxed section-title--red-box" style="top:580px">GOURMET</h2>
  <div class="col-divider" style="top:620px;height:200px"></div>

  <div class="dish col-left" style="top:622px"><div class="dish-head"><span class="dish-name">Caveman</span><span class="dots"></span><span class="price"><sup>$</sup>29</span></div><p class="dish-desc">chilli, lamb, pork sausage, chorizo, salami, bacon, spanish onion, caramelised onion, smokey bbq sauce</p></div>
  <div class="dish col-left" style="top:698px"><div class="dish-head"><span class="dish-name">Spicy Prawn &amp; Basil Presto <span class="heat"><svg width="6" height="10" viewBox="0 0 6 10"><path d="M4 0 C6 3 5 8 1 10 C3 7 3 4 4 0Z" fill="#c2603e"/></svg></span></span><span class="dots"></span><span class="price"><sup>$</sup>29</span></div><p class="dish-desc">prawns, roasted capsicum, chilli, spring onion, basil pesto</p></div>
  <div class="dish col-left" style="top:746px"><div class="dish-head"><span class="dish-name">Gourmet Vegetarian <span class="veg">v</span></span><span class="dots"></span><span class="price"><sup>$</sup>29</span></div><p class="dish-desc" style="width:215px">pumpkin, eggplant, semi-dried tomatoes, roasted capsicum, red onion, bulgarian feta, kalamata olives, spinach</p></div>

  <div class="dish col-right" style="top:622px;left:352px;width:264px"><div class="dish-head"><span class="dish-name">Jimmy Blaze <span class="heat"><svg width="6" height="10" viewBox="0 0 6 10"><path d="M4 0 C6 3 5 8 1 10 C3 7 3 4 4 0Z" fill="#c2603e"/></svg><svg width="6" height="10" viewBox="0 0 6 10"><path d="M4 0 C6 3 5 8 1 10 C3 7 3 4 4 0Z" fill="#c2603e"/></svg></span></span><span class="dots"></span><span class="price"><sup>$</sup>29</span></div><p class="dish-desc">chilli jam, jalapeno peppers, mushrooms, bacon, chilli, chorizo, spanish onion</p></div>
  <div class="dish col-right" style="top:687px;left:352px;width:264px"><div class="dish-head"><span class="dish-name">Lamb Pizza</span><span class="dots"></span><span class="price"><sup>$</sup>29</span></div><p class="dish-desc">lamb, red onion, fresh tomato, tzatziki, spring onion</p></div>
  <div class="dish col-right" style="top:739px;left:352px;width:264px"><div class="dish-head"><span class="dish-name">Los Pollos</span><span class="dots"></span><span class="price"><sup>$</sup>29</span></div><p class="dish-desc">chicken, pumpkin, basil pesto, spinach, feta, pine nuts</p></div>
  <div class="dish col-right" style="top:784px;left:352px;width:264px"><div class="dish-head"><span class="dish-name">Seafood Pizza</span><span class="dots"></span><span class="price"><sup>$</sup>29</span></div><p class="dish-desc">array of seafood</p></div>

  <p class="allergy-note"><strong>Allergies? Please let us know!</strong> All care is taken to cater for allergies including gluten, however our kitchen is small and we do not have separate preparation or cooking areas. As such, there is risk of cross-contact with your allergen and we are unable to guarantee allergen-free meals. Olives may very rarely contain pips.</p>

  <div class="legend"><span><span class="sq sq--green"></span><span class="veg">V</span> - Vegetarian</span><span>Gluten Free base <span class="extra">+$4</span></span><span>Vegan Cheese <span class="extra">+$3</span></span></div>
</section>

</body>
</html>
```